Letterhead

Can you please design me a letterhead that I can use electronically in word as a template. I have attached my business card as I would like the design to reflect this logo.

```html
<!DOCTYPE html>
<html lang="en">
<head>
<meta charset="utf-8">
<title>Meridale Business Consultants – Letterhead</title>
<link rel="stylesheet" href="https://fonts.googleapis.com/css2?family=Open+Sans:wght@400;600&display=swap">
<style>
  :root {
    --bg-light: #f4f4f4;
    --bg-dark: #d6d6d6;
    --sheet-white: #ffffff;
    --sheet-black: #1f1b1a;
    --brand-red: #a32424;
    --brand-red-faint: #3b1c1b;
    --ink: #1a1a1a;
    --ink-soft: #4a4a4a;
  }
  * { margin: 0; padding: 0; box-sizing: border-box; }
  html, body {
    width: 1200px;
    height: 993px;
    overflow: hidden;
  }
  body {
    background: radial-gradient(ellipse at 50% 40%, var(--bg-light) 0%, var(--bg-dark) 100%);
    font-family: "Open Sans", Arial, sans-serif;
    position: relative;
  }
  .sheet {
    position: absolute;
    top: 143px;
    width: 500px;
    height: 707px;
    box-shadow: 0 6px 18px rgba(0, 0, 0, 0.25);
  }

  /* Reverse side */
  .sheet--reverse {
    left: 90px;
    background: var(--sheet-black);
    overflow: hidden;
  }
  .reverse-wordmark {
    position: absolute;
    top: 300px;
    left: 0;
    width: 100%;
    text-align: center;
    font-size: 96px;
    font-weight: 600;
    letter-spacing: -1px;
    color: var(--brand-red-faint);
    line-height: 1;
  }

  /* Letterhead front */
  .sheet--letterhead {
    left: 610px;
    background: var(--sheet-white);
  }
  .masthead {
    position: absolute;
    top: 56px;
    left: 0;
    width: 100%;
    text-align: center;
    padding-left: 70px;
  }
  .masthead__name {
    display: block;
    font-size: 44px;
    font-weight: 600;
    letter-spacing: -0.5px;
    line-height: 1;
    color: var(--brand-red);
  }
  .masthead__tagline {
    display: block;
    margin-top: 4px;
    font-size: 9.5px;
    color: var(--ink);
  }
  .contact-line {
    position: absolute;
    bottom: 54px;
    left: 0;
    width: 100%;
    text-align: center;
    font-size: 10px;
    color: var(--ink-soft);
  }
  .contact-line .label { color: var(--brand-red); }
  .contact-line .sep { color: var(--brand-red); margin: 0 4px; }
  .footer-band {
    position: absolute;
    bottom: 0;
    left: 0;
    width: 100%;
    height: 34px;
    display: flex;
  }
  .footer-band__red { flex: 1; background: var(--brand-red); }
  .footer-band__black { width: 70px; background: var(--sheet-black); }
</style>
</head>
<body>
  <section class="sheet sheet--reverse" aria-label="Letterhead reverse side">
    <p class="reverse-wordmark">meridale</p>
  </section>

  <section class="sheet sheet--letterhead" aria-label="Letterhead front">
    <header class="masthead">
      <span class="masthead__name">meridale</span>
      <span class="masthead__tagline">Business Consultants Pty Ltd</span>
    </header>

    <p class="contact-line">
      <span class="label">P</span> : 0400 555 018<span class="sep">|</span><span class="label">E</span> : helen@meridale.net.au<span class="sep">|</span><span class="label">ACN</span> : 000 111 222
    </p>

    <div class="footer-band">
      <div class="footer-band__red"></div>
      <div class="footer-band__black"></div>
    </div>
  </section>
</body>
</html>
```